iPad Apps for Energy Industry w/ IT Consulting Business Needs a Brochure Design

We need a brochure and business card design for an IT development and consulting company based in Westlake Village, CA called "Copperfield Systems". We develop innovative iPad apps and provide IT consulting services for the Energy industry (specifically Oil and Gas companies).

For consulting services, we provide Business Intelligence solutions to implement Data Warehouse strategies. Our services include Business Intelligence, Data Warehouse, Application Integration and Support. An older consulting brochure we have used in the past under a different company name ("Norwell Data Advisory") is attached for additional background and content. We do not want to use the old design at all - its really just for reference only.

Our first product is called "Fieldpoint KRV" - includes iPad apps and web-based tools that support field production data gathering for Oil and Gas companies. It also includes a Decision Support Center (DSC) to help with route management of field operators using mapping technologies.

The final design should be an overview of the company, products and services with contact information.
Updates

We included some sample content for the areas of company overview, products and services for the brochure (added to attachment area - "Sample Content").  If there is too much content for your design, you do not need to use all of the sample.  We are flexible to re-write all areas to fit the design.

Please let us know if you need more information or have any additional questions about the brochure.

Contact information for the brochure below - 

4187 Halberton Ave. Suite 310
Westlake Village, CA. 91488
United States

+1-805-555-0173
info@copperfieldsystems-example.com
http://www.copperfieldsystems-example.com 

Please Note: Our website above is currently a placeholder, feel free to reference our previous site for additional details -  http://www.norwelldata-example.com

Target Market(s)

Oil and Gas company managers, males between 40 - 55 years old in corporate sector, college education, technical backgrounds

Industry/Entity Type

Industry

Requirements
Must have
• The bi-fold brochure must have 4 pages. It should measure 11" x 17" - folding to 8 1/2" x 11" for each page.
Nice to have
• We have a starter idea for the logo, but we would love to see other ideas. The starter logo ideas are attached but feel free to change it, thanks!

We would love the brochure to have different areas to highlight the company, products and services in an interesting way or layout. It should accommodate a good balance between photos/images and text but the brochure is an overview only of the products and services.

```html
<!DOCTYPE html>
<html lang="en">
<head>
<meta charset="utf-8">
<title>Copperfield Systems – Brochure Spread</title>
<link href="https://fonts.googleapis.com/css2?family=Source+Sans+3:wght@400;600;700&display=swap" rel="stylesheet">
<style>
  :root {
    --blue-dark: #0c4a8f;
    --blue-mid: #1a6fb8;
    --blue-light: #2e9fdc;
    --orange: #f05a28;
    --orange-light: #f7931e;
    --gold: #f6b333;
    --ink: #333333;
    --grey: #555555;
    --page-bg: #e9e9e9;
    --white: #ffffff;
  }
  * { box-sizing: border-box; margin: 0; padding: 0; }
  html, body { width: 1200px; height: 960px; overflow: hidden; }
  body {
    background: var(--page-bg);
    font-family: "Source Sans 3", "Myriad Pro", Arial, sans-serif;
    color: var(--ink);
    position: relative;
  }
  .spread {
    position: absolute;
    left: 20px; top: 105px;
    width: 1160px; height: 750px;
    display: flex;
    background: var(--white);
    box-shadow: 0 6px 24px rgba(0,0,0,.25);
  }
  .panel { position: relative; width: 580px; height: 750px; overflow: hidden; }
  .panel--back { border-right: 1px solid #d4d4d4; }

  /* back panel */
  .photo-strip { position: absolute; left: 0; top: 0; width: 580px; height: 183px; display: flex; }
  .photo--refinery-night { width: 295px; height: 100%; background: linear-gradient(180deg, #2a2f5c 0%, #4a4f7a 55%, #b8a57a 100%); }
  .photo--plant-engineers { width: 285px; height: 100%; background: linear-gradient(180deg, #c9cdd2 0%, #8d939a 60%, #3d4f78 100%); }
  .accent-rule { position: absolute; left: 0; top: 183px; width: 100%; height: 6px; background: linear-gradient(90deg, var(--orange), var(--orange-light)); }
  .overview {
    position: absolute; left: 0; top: 189px; width: 580px; height: 393px;
    background: linear-gradient(100deg, var(--blue-dark) 0%, var(--blue-mid) 55%, var(--blue-light) 100%);
    color: var(--white);
  }
  .overview__title {
    position: absolute; left: 64px; top: 61px;
    font-size: 19px; font-weight: 700; color: var(--gold);
    padding-bottom: 6px; border-bottom: 1px dashed rgba(255,255,255,.6);
    width: 164px;
  }
  .overview__body { position: absolute; left: 64px; top: 122px; width: 458px; font-size: 11.2px; line-height: 13.8px; }
  .overview__body p { margin-bottom: 15px; text-align: justify; }
  .arrows { position: absolute; }
  .arrows--back { left: 472px; top: 557px; }
  .arrows--front { left: 464px; top: 163px; }

  .contact { position: absolute; left: 0; top: 582px; width: 580px; height: 143px; }
  .brand-mark { display: flex; align-items: center; gap: 8px; }
  .brand-mark__dot { width: 26px; height: 26px; border-radius: 50%; background: var(--orange-light); flex: none; }
  .brand-mark__name { font-weight: 600; color: var(--blue-dark); white-space: nowrap; }
  .brand-mark__tag { color: var(--grey); border-left: 1px solid #999; padding-left: 6px; line-height: 1.1; }
  .contact .brand-mark { position: absolute; left: 198px; top: 14px; }
  .contact .brand-mark__name { font-size: 17px; }
  .contact .brand-mark__tag { font-size: 8px; }
  .contact__address { position: absolute; right: 312px; top: 72px; text-align: right; font-size: 11px; line-height: 14px; padding-right: 14px; border-right: 1px solid var(--orange); }
  .contact__lines { position: absolute; left: 296px; top: 82px; font-size: 11px; line-height: 14px; }

  .footer-bar {
    position: absolute; left: 0; bottom: 0; width: 100%; height: 25px;
    background: linear-gradient(90deg, var(--orange), var(--orange-light));
    color: var(--white); font-size: 11.5px;
    display: flex; align-items: center; justify-content: center; gap: 30px;
  }
  .footer-bar__sep { width: 1px; height: 15px; background: var(--white); }

  /* front panel */
  .masthead { position: absolute; left: 0; top: 0; width: 580px; height: 183px; display: flex; align-items: center; justify-content: center; }
  .masthead .brand-mark { gap: 12px; }
  .masthead .brand-mark__dot { width: 58px; height: 58px; }
  .masthead .brand-mark__name { font-size: 30px; }
  .masthead .brand-mark__tag { font-size: 16px; padding-left: 10px; }
  .photo--field-crew {
    position: absolute; left: 0; top: 189px; width: 580px; height: 393px;
    background: linear-gradient(180deg, #7fb4e3 0%, #cfe0ee 38%, #c9b98e 62%, #8a7a55 80%, #2b2b2b 100%);
  }
  .headline { position: absolute; left: 0; top: 637px; width: 100%; text-align: center; font-size: 30px; font-weight: 700; color: var(--blue-dark); letter-spacing: .3px; }
  .panel--front .footer-bar { justify-content: flex-end; padding-right: 92px; }
</style>
</head>
<body>
<main class="spread">
  <section class="panel panel--back">
    <div class="photo-strip">
      <div class="photo--refinery-night" role="img" aria-label="Photo of a refinery lit up at night"></div>
      <div class="photo--plant-engineers" role="img" aria-label="Photo of two engineers in hard hats at a processing plant"></div>
    </div>
    <div class="accent-rule"></div>
    <div class="overview">
      <h2 class="overview__title">Company Overview</h2>
      <div class="overview__body">
        <p>Copperfield Systems is dedicated to building a relationship with partners by sharing a common goal of delivering the highest quality customer satisfaction.</p>
        <p>Copperfield Systems will assess the company’s current data needs and determine an information management strategy. Because every business sector is unique, Copperfield Systems assesses each individual department’s current reporting and data requirements. We will provide an incremental solution based on business timelines and expectations.</p>
        <p>We leverage your current infrastructure to provide a central solution for your reporting and information needs. In addition, training will be offered to user groups to learn the new reporting solutions. From implementation, execution, and post IT support, Copperfield Systems delivers full service to all partners.</p>
      </div>
    </div>
    <svg class="arrows arrows--back" width="96" height="48" viewBox="0 0 96 48" aria-hidden="true">
      <polygon points="0,14 20,24 0,34" fill="#f7931e"/>
      <polygon points="27,8 54,24 27,40" fill="#f58220"/>
      <polygon points="62,0 96,24 62,48" fill="#f26522"/>
    </svg>
    <div class="contact">
      <div class="brand-mark">
        <span class="brand-mark__dot"></span>
        <span class="brand-mark__name">Copperfield Systems</span>
        <span class="brand-mark__tag">Creative Solutions<br>For Oil And Gas</span>
      </div>
      <address class="contact__address" style="font-style:normal">4187 Halberton Ave. Suite 310<br>Westlake Village, CA. 91488<br>United States</address>
      <div class="contact__lines">Call: +1-805-555-0173<br>Email: info@copperfieldsystems-example.com</div>
    </div>
    <footer class="footer-bar"><span>www.copperfieldsystems-example.com</span></footer>
  </section>

  <section class="panel panel--front">
    <header class="masthead">
      <div class="brand-mark">
        <span class="brand-mark__dot"></span>
        <span class="brand-mark__name">Copperfield Systems</span>
        <span class="brand-mark__tag">Creative Solutions<br>For Oil And Gas</span>
      </div>
    </header>
    <div class="accent-rule"></div>
    <div class="photo--field-crew" role="img" aria-label="Photo of two field workers in hard hats and safety vests with a laptop beside an oil pump jack"></div>
    <svg class="arrows arrows--front" width="96" height="48" viewBox="0 0 96 48" aria-hidden="true">
      <polygon points="0,14 20,24 0,34" fill="#1d5fa8"/>
      <polygon points="27,8 54,24 27,40" fill="#1f78c1"/>
      <polygon points="62,0 96,24 62,48" fill="#2a8fd4"/>
    </svg>
    <h1 class="headline">Creative Solutions For Oil And Gas</h1>
    <footer class="footer-bar">
      <span>Call Us Today : +1-805-555-0173</span>
      <span class="footer-bar__sep"></span>
      <span>www.copperfieldsystems-example.com</span>
    </footer>
  </section>
</main>
</body>
</html>
```